Business card por a urban DJ, up scale audience target

Need a sober design, modern, conservative colors but i can consider some options, y play rnb, hip hop, EDM and top40.

Business card for contact and personal info, double sided, use logo attrached please; im 42 so i need a card acording to my age an target audience.

Target Market(s)

Adult people, up scale audience

Industry/Entity Type

Music Download

Contact Information for Business Card

Cel (318) 5024471963 www.kelvarodun.com

Requirements
Must have
• open mind
Nice to have
• open mind
Should not have
• DJ

```html
<!DOCTYPE html>
<html lang="en">
<head>
<meta charset="utf-8">
<title>KELVA – DJ Business Card</title>
<link rel="stylesheet" href="https://fonts.googleapis.com/css2?family=Oswald:wght@500;700&family=Open+Sans:wght@700;800&display=swap">
<style>
  :root {
    --backdrop: #d9d9d9;
    --card-dark: #15171a;
    --card-blue: #0a4fa0;
    --steel: #c9d1d8;
    --accent-blue: #1e5fb3;
    --tag-blue: #2a6fc2;
    --ink-dark: #141820;
    --white: #ffffff;
  }
  html, body {
    margin: 0;
    width: 1200px;
    height: 900px;
    overflow: hidden;
    background: var(--backdrop);
  }
  .canvas {
    position: relative;
    width: 1200px;
    height: 900px;
  }
  .card {
    position: absolute;
    left: 250px;
    width: 700px;
    height: 400px;
    box-sizing: border-box;
    box-shadow: 0 6px 18px rgba(0,0,0,0.25);
  }
  .card--front {
    top: 35px;
    background: var(--card-dark);
  }
  .card--back {
    top: 465px;
    background: var(--card-blue);
  }
  .brand-name {
    font-family: "Oswald", sans-serif;
    font-weight: 700;
    color: var(--steel);
    letter-spacing: 0.04em;
    margin: 0;
    line-height: 1;
  }
  .card--front .brand-name {
    position: absolute;
    left: 0;
    right: 0;
    top: 60px;
    text-align: center;
    font-size: 150px;
  }
  .tagline {
    position: absolute;
    left: 110px;
    top: 262px;
    margin: 0;
    font-family: "Oswald", sans-serif;
    font-weight: 500;
    font-size: 22px;
    letter-spacing: 0.05em;
    color: var(--tag-blue);
  }
  .dj-name {
    position: absolute;
    right: 105px;
    top: 300px;
    margin: 0;
    font-family: "Open Sans", sans-serif;
    font-weight: 700;
    font-size: 21px;
    color: var(--accent-blue);
  }
  .card--back .brand-name {
    position: absolute;
    left: 150px;
    top: 120px;
    font-size: 96px;
  }
  .contact {
    position: absolute;
    left: 385px;
    top: 230px;
    margin: 0;
    font-family: "Open Sans", sans-serif;
    font-weight: 800;
    font-size: 28px;
    color: var(--white);
    white-space: nowrap;
  }
  .contact__label {
    color: var(--ink-dark);
  }
</style>
</head>
<body>
  <main class="canvas">
    <section class="card card--front" aria-label="Card front">
      <h1 class="brand-name">KELVA</h1>
      <p class="tagline">Y PLAY RNB, HIP HOP, EDM AND TOP40</p>
      <p class="dj-name">DJ Marcus T Ellery</p>
    </section>
    <section class="card card--back" aria-label="Card back">
      <p class="brand-name">KELVA</p>
      <p class="contact"><span class="contact__label">CELL:</span> 850-555-0192</p>
    </section>
  </main>
</body>
</html>
```